Business Card for Managing Partner Investment Fund

To create a business card template for an investment fund manager. Business card should be more professional in nature, not too colorful, more upscale, and created using the attached logos and fund name files. I would prefer a black or gray color scheme, but am open to the use of color as well. I would prefer a double sided business card, but open to single sided business card designs as well. The business card should include: name, title, and contact information, as well as logo and company name. I would prefer a more stream-lined, simple business card design.
Updates
Address: 4190 NE 38th Ter. Ocala, FL 34470
Email: talvin47@quorimail.net
Phone: 561-347-9162
Title: managing partner
Name: Dorian Velsky
Fund Name: Ambergate Capital
Logos can be found in files attached to the brief
Target Market(s)
potential investors, other fund managers
Industry/Entity Type
Finance
Contact Information for Business Card
Name on card: Dorian Velsky
Title: Managing Partner
Colors
Designer to choose colors to be used in the design.
Requirements
Must have
- Phone number
- email address
- physical address
- title
- name
- logo
- Fund name
Nice to have
- simple layout
Should not have
- too many colors, busy fonts,

```html
<!DOCTYPE html>
<html lang="en">
<head>
<meta charset="utf-8">
<title>Ambergate Capital – Business Card</title>
<link rel="stylesheet" href="https://fonts.googleapis.com/css2?family=Cinzel:wght@500&family=Roboto:wght@400;700&display=swap">
<style>
  :root {
    --backdrop: #2b1c16;
    --card-grey: #727272;
    --card-black: #070909;
    --ink: #0c0c0c;
    --ink-soft: #1a1a1a;
    --logo-grey: #b9b9b9;
    --deco-dark: #0a0a0a;
  }
  * { margin: 0; padding: 0; box-sizing: border-box; }
  html, body { width: 1200px; height: 1000px; overflow: hidden; }
  body {
    background: var(--backdrop);
    font-family: "Roboto", Arial, sans-serif;
    position: relative;
  }
  .card {
    position: absolute;
    width: 460px;
    height: 268px;
    box-shadow: 0 6px 18px rgba(0,0,0,.35);
  }
  /* Front side */
  .card-front {
    left: 110px;
    top: 366px;
    background: var(--card-grey);
    overflow: hidden;
  }
  .front-decor {
    position: absolute;
    right: 0;
    bottom: 0;
    width: 290px;
    height: 170px;
    background: linear-gradient(160deg, var(--deco-dark) 0%, #1c1c1c 100%);
    clip-path: polygon(100% 0, 100% 100%, 0 100%);
  }
  .address {
    position: absolute;
    top: 22px;
    right: 26px;
    display: flex;
    gap: 8px;
    font-size: 11.5px;
    line-height: 1.35;
    color: var(--ink-soft);
  }
  .identity {
    position: absolute;
    left: 34px;
    top: 96px;
  }
  .person-name {
    font-weight: 700;
    font-size: 19px;
    color: var(--ink);
    letter-spacing: .2px;
  }
  .person-title {
    font-size: 11.5px;
    color: var(--ink-soft);
    margin-top: 1px;
  }
  .contact-list {
    list-style: none;
    margin-top: 14px;
    font-size: 11.5px;
    color: var(--ink-soft);
  }
  .contact-list li {
    display: flex;
    align-items: center;
    gap: 8px;
    height: 17px;
  }
  .icon { width: 11px; height: 11px; flex: none; fill: var(--ink); }
  /* Back side */
  .card-back {
    left: 630px;
    top: 366px;
    background: var(--card-black);
    display: flex;
    flex-direction: column;
    align-items: center;
    justify-content: center;
  }
  .brand-name {
    font-family: "Cinzel", "Times New Roman", serif;
    font-weight: 500;
    color: var(--logo-grey);
    text-align: center;
    font-size: 27px;
    letter-spacing: 1.5px;
    line-height: 1.15;
  }
  .brand-name span { display: block; font-size: 16px; letter-spacing: 4px; }
</style>
</head>
<body>
  <section class="card card-front" aria-label="Business card front">
    <div class="front-decor" role="img" aria-label="Dark mountain-range decoration area"></div>

    <div class="address">
      <svg class="icon" viewBox="0 0 24 24" aria-hidden="true"><path d="M12 2a7 7 0 0 0-7 7c0 5 7 13 7 13s7-8 7-13a7 7 0 0 0-7-7zm0 9.5A2.5 2.5 0 1 1 12 6.5a2.5 2.5 0 0 1 0 5z"/></svg>
      <p>4190 NE 38th Ter.<br>Ocala, FL 34470</p>
    </div>

    <div class="identity">
      <h1 class="person-name">Dorian Velsky</h1>
      <p class="person-title">Managing Partner</p>
      <ul class="contact-list">
        <li>
          <svg class="icon" viewBox="0 0 24 24" aria-hidden="true"><path d="M6.6 10.8a15 15 0 0 0 6.6 6.6l2.2-2.2a1 1 0 0 1 1-.25 11.4 11.4 0 0 0 3.6.57 1 1 0 0 1 1 1V20a1 1 0 0 1-1 1A17 17 0 0 1 3 4a1 1 0 0 1 1-1h3.5a1 1 0 0 1 1 1c0 1.25.2 2.45.57 3.57a1 1 0 0 1-.25 1z"/></svg>
          561-347-9162
        </li>
        <li>
          <svg class="icon" viewBox="0 0 24 24" aria-hidden="true"><path d="M2 5h20v14H2zm2 2v.5l8 5 8-5V7l-8 5z"/></svg>
          talvin47@quorimail.net
        </li>
        <li>
          <svg class="icon" viewBox="0 0 24 24" aria-hidden="true"><path d="M12 2a10 10 0 1 0 0 20 10 10 0 0 0 0-20zm6.9 6h-3a15 15 0 0 0-1.4-3.9A8 8 0 0 1 18.9 8zM12 4c.8 1.2 1.5 2.5 1.9 4h-3.8c.4-1.5 1.1-2.8 1.9-4zM4.3 14a8 8 0 0 1 0-4h3.4a16 16 0 0 0 0 4zm.8 2h3a15 15 0 0 0 1.4 3.9A8 8 0 0 1 5.1 16zm3-8h-3a8 8 0 0 1 4.4-3.9A15 15 0 0 0 8.1 8zM12 20c-.8-1.2-1.5-2.5-1.9-4h3.8c-.4 1.5-1.1 2.8-1.9 4zm2.3-6H9.7a14 14 0 0 1 0-4h4.6a14 14 0 0 1 0 4zm.2 5.9A15 15 0 0 0 15.9 16h3a8 8 0 0 1-4.4 3.9zm1.8-5.9a16 16 0 0 0 0-4h3.4a8 8 0 0 1 0 4z"/></svg>
          www.ambergatecapital.net
        </li>
      </ul>
    </div>
  </section>

  <section class="card card-back" aria-label="Business card back">
    <p class="brand-name">Ambergate<span>Capital</span></p>
  </section>
</body>
</html>
```